Business Card Design

We are a Sydney based bespoke Concierge company, providing hospitality services including Concierge staffing, catering, home dining, events, delivery, passwright, and manage desks in residential apartment services. Our website goes into more detail.

Target Market(s)

corporate clients, upscale residential clients, executives,

Industry/Entity Type

Hospitality

Contact Information for Business Card

David SouthwellDirector of Operations & Customer Experience
Larkmoor Concierge
W:www.larkmoorconcierge.net;
E;martin@larkmoorconcierge.net
M: 0491 570 213

Font styles to use
Serif

Colors
3176b5
85cae6
d2a4cc
6b449b

Requirements
Must have
• Business name
• Name
• Title
• Tel
• Email
• Website
Nice to have
• Back - facebook , twitter, instagram

```html
<!DOCTYPE html>
<html lang="en">
<head>
<meta charset="utf-8">
<title>Larkmoor Concierge — Business Card</title>
<link rel="stylesheet" href="https://fonts.googleapis.com/css2?family=Cinzel:wght@400;500&display=swap">
<style>
  :root {
    --canvas: #ffffff;
    --purple-deep: #6b449b;
    --purple-soft: #9678b8;
    --magenta: #ec008c;
    --magenta-deep: #c01b70;
    --sky: #85cae6;
    --sky-deep: #74b2cf;
    --blush: #f1c9e0;
    --blush-deep: #d2a4cc;
    --ink-light: #ffffff;
  }
  html, body {
    margin: 0;
    padding: 0;
    width: 1200px;
    height: 1000px;
    overflow: hidden;
    background: var(--canvas);
  }
  .stage {
    position: relative;
    width: 1200px;
    height: 1000px;
  }
  .card {
    position: absolute;
    left: 326px;
    width: 548px;
    height: 325px;
    filter: drop-shadow(6px 8px 7px rgba(0, 0, 0, 0.28));
  }
  .card--front { top: 120px; }
  .card--back { top: 537px; }
  .card text {
    font-family: "Cinzel", serif;
    fill: var(--ink-light);
  }
  .person-name { font-size: 30px; letter-spacing: 0.5px; }
  .person-title { font-size: 13px; }
  .contact-phone { font-size: 15px; }
  .contact-line { font-size: 12px; }
  .brand-word { font-size: 50px; }
  .brand-word--sub { font-size: 38px; }
  .brand-mark-name { font-size: 10px; font-weight: 500; }
  .social-handle { font-size: 8.5px; }
  .social-chip { fill: var(--ink-light); }
</style>
</head>
<body>
<main class="stage">

  <!-- Front: personal details -->
  <svg class="card card--front" viewBox="0 0 548 325" aria-label="Business card front">
    <defs>
      <clipPath id="front-shape"><rect width="548" height="325" rx="22"/></clipPath>
      <linearGradient id="front-purple" x1="0" y1="0" x2="0" y2="1">
        <stop offset="0" stop-color="var(--purple-deep)"/>
        <stop offset="1" stop-color="var(--purple-soft)"/>
      </linearGradient>
      <linearGradient id="front-magenta" x1="0" y1="0" x2="0" y2="1">
        <stop offset="0" stop-color="var(--magenta-deep)"/>
        <stop offset="0.45" stop-color="var(--magenta)"/>
      </linearGradient>
      <linearGradient id="front-sky" x1="0" y1="0" x2="1" y2="0.3">
        <stop offset="0" stop-color="var(--sky-deep)"/>
        <stop offset="0.5" stop-color="var(--sky)"/>
      </linearGradient>
      <linearGradient id="front-blush" x1="0" y1="0" x2="1" y2="0">
        <stop offset="0" stop-color="var(--blush-deep)"/>
        <stop offset="0.6" stop-color="var(--blush)"/>
      </linearGradient>
    </defs>
    <g clip-path="url(#front-shape)">
      <rect class="band band--purple" width="548" height="325" fill="url(#front-purple)"/>
      <polygon class="band band--magenta" points="227,0 350,0 548,207 548,325 322,325" fill="url(#front-magenta)"/>
      <polygon class="band band--sky" points="350,0 548,0 548,207" fill="url(#front-sky)"/>
      <polygon class="band band--blush" points="0,123 174,325 0,325" fill="url(#front-blush)"/>
    </g>

    <g class="brand-mark">
      <circle cx="40" cy="40" r="27" fill="var(--ink-light)"/>
      <text class="brand-mark-name" x="74" y="44">Larkmoor Concierge</text>
    </g>

    <text class="person-name" x="274" y="163" text-anchor="middle">MARTIN ASHGROVE</text>
    <text class="person-title" x="274" y="183" text-anchor="middle">Director of Operations &amp; Customer Experience</text>

    <text class="contact-phone" x="534" y="244" text-anchor="end">M: 0491 570 213</text>
    <text class="contact-line" x="532" y="271" text-anchor="end">WEB : WWW.LARKMOORCONCIERGE.NET</text>
    <text class="contact-line" x="532" y="297" text-anchor="end">E-MAIL : MARTIN@LARKMOORCONCIERGE.NET</text>
  </svg>

  <!-- Back: business name and social handles -->
  <svg class="card card--back" viewBox="0 0 548 325" aria-label="Business card back">
    <defs>
      <clipPath id="back-shape"><rect width="548" height="325" rx="22"/></clipPath>
      <linearGradient id="back-purple" x1="0" y1="0" x2="0" y2="1">
        <stop offset="0" stop-color="var(--purple-soft)"/>
        <stop offset="1" stop-color="var(--purple-deep)"/>
      </linearGradient>
      <linearGradient id="back-magenta" x1="0" y1="0" x2="0" y2="1">
        <stop offset="0.55" stop-color="var(--magenta)"/>
        <stop offset="1" stop-color="var(--magenta-deep)"/>
      </linearGradient>
      <linearGradient id="back-sky" x1="0" y1="0" x2="1" y2="0.3">
        <stop offset="0.5" stop-color="var(--sky)"/>
        <stop offset="1" stop-color="var(--sky-deep)"/>
      </linearGradient>
      <linearGradient id="back-blush" x1="0" y1="0" x2="1" y2="0">
        <stop offset="0.4" stop-color="var(--blush)"/>
        <stop offset="1" stop-color="var(--blush-deep)"/>
      </linearGradient>
    </defs>
    <g clip-path="url(#back-shape)">
      <rect class="band band--magenta" width="548" height="325" fill="url(#back-magenta)"/>
      <polygon class="band band--purple" points="227,0 374,0 548,203 548,325 294,325" fill="url(#back-purple)"/>
      <polygon class="band band--blush" points="374,0 548,0 548,203" fill="url(#back-blush)"/>
      <polygon class="band band--sky" points="0,118 199,325 0,325" fill="url(#back-sky)"/>
    </g>

    <g class="brand-mark">
      <circle cx="50" cy="47" r="27" fill="var(--ink-light)"/>
      <text class="brand-mark-name" x="84" y="51">Larkmoor Concierge</text>
    </g>

    <text class="brand-word" x="274" y="143" text-anchor="middle">Larkmoor</text>
    <text class="brand-word brand-word--sub" x="274" y="191" text-anchor="middle">Concierge</text>

    <g class="social">
      <rect class="social-chip" x="78" y="275" width="16" height="16" rx="2"/>
      <text class="social-handle" x="86" y="310" text-anchor="middle">CHIRPLINE.COM/LMSERVICE</text>

      <rect class="social-chip" x="245" y="275" width="16" height="16" rx="2"/>
      <text class="social-handle" x="253" y="310" text-anchor="middle">FACEPAGE.COM/LARKMOOR-CONCIERGE</text>

      <rect class="social-chip" x="431" y="275" width="16" height="16" rx="2"/>
      <text class="social-handle" x="439" y="310" text-anchor="middle">SNAPGRAM.COM/LARKMOOR_CONCIERGE</text>
    </g>
  </svg>

</main>
</body>
</html>
```